Business Card Design

After a corporate career in the finance sector I am now operating on my own as a consultant. I require a simple design, and want a strong card which is targeted at a conservative audience.

Target Market(s)

highly educated senior management, directors of companies, finance sector

Industry/Entity Type

Conservative

Contact Information for Business Card

Ruth Danver
Consultant
Mobile: 0417 862 450
Email: ruth.danv@mailcove.net

Requirements
Should not have
• I don't want the colours green/yellow/brown

```html
<!DOCTYPE html>
<html lang="en">
<head>
<meta charset="utf-8">
<title>Ruth Danver – Consultant</title>
<link rel="stylesheet" href="https://fonts.googleapis.com/css2?family=Strait&family=Varela+Round&display=swap">
<style>
  :root {
    --brand-teal: #2a97a3;
    --paper: #ffffff;
    --shadow-grey: rgba(0, 0, 0, 0.3);
  }
  html, body {
    margin: 0;
    padding: 0;
    width: 1200px;
    height: 741px;
    overflow: hidden;
    background: var(--paper);
  }
  .card {
    position: relative;
    width: 1200px;
    height: 741px;
    background: var(--paper);
    overflow: hidden;
  }
  .band-top {
    position: absolute;
    left: 0; top: 0;
    width: 1200px; height: 82px;
    background: var(--brand-teal);
  }
  .band-bottom {
    position: absolute;
    left: 0; top: 552px;
    width: 1200px; height: 189px;
    background: var(--brand-teal);
  }
  .name {
    position: absolute;
    left: 0; top: 196px;
    width: 1210px;
    margin: 0;
    text-align: center;
    font-family: "Strait", sans-serif;
    font-weight: 400;
    font-size: 112px;
    line-height: 1;
    letter-spacing: 1px;
    color: var(--brand-teal);
    text-transform: uppercase;
    text-shadow: 4px 6px 5px var(--shadow-grey);
    white-space: nowrap;
  }
  .role {
    position: absolute;
    left: 0; top: 312px;
    width: 1200px;
    margin: 0;
    text-align: center;
    font-family: "Strait", sans-serif;
    font-size: 34px;
    line-height: 1;
    letter-spacing: 4px;
    color: var(--brand-teal);
    text-transform: uppercase;
  }
  .contact {
    position: absolute;
    left: 510px; top: 562px;
    margin: 0;
    font-family: "Varela Round", sans-serif;
    font-size: 33px;
    line-height: 44px;
    color: var(--paper);
  }
  .contact-row {
    display: flex;
    white-space: nowrap;
  }
  .contact-label {
    width: 147px;
  }
  .contact-row--email .contact-label {
    width: 153px;
  }
  .contact-value {
    margin: 0;
  }
</style>
</head>
<body>
  <main class="card">
    <div class="band-top"></div>
    <h1 class="name">Ruth&nbsp;&nbsp;Danver</h1>
    <p class="role">Consultant</p>
    <div class="band-bottom"></div>
    <dl class="contact">
      <div class="contact-row contact-row--mobile">
        <dt class="contact-label">mobile</dt>
        <dd class="contact-value">0417 862 450</dd>
      </div>
      <div class="contact-row contact-row--email">
        <dt class="contact-label">email</dt>
        <dd class="contact-value">ruth.danv@mailcove.net</dd>
      </div>
    </dl>
  </main>
</body>
</html>
```